Buch-/eBook-Cover zum Thema Ökonomie
Ribo hat mit seinem Design genau meine Vorstellung getroffen! Einen Stern gibt's dafür Abzug, dass die verwendeten Programme und Fotos etc erst nach dem Zuschlag bekanntgegeben wurden - das hätte auch gleich transparent sein können. Aber grundsätzlich bin ich sehr zufrieden.
Zielgruppe
Ich bin mehrfacher Buchautor und Philosoph. Meine Zielgruppe hier sind jene, die sich für Ökonomie interessieren.
Aufgabenstellung
Ich will mein Buch 'Der Kreislauf der Nachfrage. Keiner bringt uns das Brot' auf Verlo BDS im Selfpublishing herausbringen. Dafür brauche ich eine druckfähige PDF-Datei. Ich habe Spezifikationen für die exakten Größen- und Seitenverhältnisse, die ich hochlade. Außerdem habe ich ein Logo (meine Q3T!), das an geeigneter Stelle auf dem Cover zu platzieren ist. Ich stelle mir grundsätzlich ein Bild von einer dominanten Spielfigur (wie beim Hüpf-und-schlag-den-Turm) vor, die auf einem Spielbrett steht, vielleicht mit anderen Spielfiguren im Hintergrund. Außerdem müssen Titel, Untertitel und mein Name (Konrad Edmund Wiesheimer) gut lesbar sein. Als Klappentext habe ich:
'Die Ökonomie beginnt nicht beim Markt – sie beginnt bei Ihnen.
Dieses Buch behauptet etwas Unverschämtes: Unsere Wirtschaft basiert auf der stillen Erwartung, dass jemand anderer uns füttert.
Wer das einmal sieht, versteht plötzlich Krisen, Macht und Wohlstand auf eine neue, fast unangenehme Weise.
Konrad Edmund Wiesheimer dreht die Perspektive radikal um – vom Verbraucher aus gedacht, bis nichts mehr selbstverständlich bleibt.
Ein Buch für alle, die nicht länger so tun wollen, als hätten sie mit dem Ganzen nichts zu tun.'
Ansonsten hoffe ich auf hochwertige, kreative Designergebnisse.
Das Design darf nicht zu überladen sein.

```html
<!DOCTYPE html>
<html lang="de">
<head>
<meta charset="utf-8">
<title>Der Kreislauf der Nachfrage – Buchumschlag</title>
<link rel="stylesheet" href="https://fonts.googleapis.com/css2?family=Bebas+Neue&family=Montserrat:wght@500;600&family=Ubuntu:wght@400&display=swap">
<style>
  :root {
    --page-bg: #ececec;
    --wood-dark: #3f2509;
    --wood-mid: #6b3f14;
    --wood-light: #9a6a35;
    --board-light: #d2ae78;
    --figure-blue: #2b3f86;
    --figure-blue-dark: #1c2a5e;
    --title-ivory: #ece6dc;
    --gold: #d9bf78;
    --tagline: #f1e2a0;
    --body-text: #f3ede4;
    --mark-red: #e2231a;
  }
  * { margin: 0; padding: 0; box-sizing: border-box; }
  html, body { width: 1200px; height: 974px; overflow: hidden; background: var(--page-bg); }
  .cover {
    position: absolute; left: 108px; top: 114px; width: 983px; height: 724px;
    display: flex; overflow: hidden;
  }
  .back-cover {
    position: relative; width: 470px; height: 100%;
    background: linear-gradient(180deg, var(--wood-dark) 0%, #5a3410 45%, var(--wood-mid) 75%, #5b3510 100%);
  }
  .spine {
    position: relative; width: 44px; height: 100%;
    background: linear-gradient(180deg, #2d1a06 0%, #4a2c0e 60%, #5a3813 100%);
  }
  .front-cover { position: relative; width: 469px; height: 100%; }
  .front-photo {
    position: absolute; inset: 0;
    background:
      linear-gradient(160deg, transparent 0%, transparent 55%, rgba(210,174,120,0.75) 72%, rgba(196,156,100,0.8) 100%),
      linear-gradient(180deg, var(--wood-dark) 0%, #6a4015 30%, var(--wood-light) 55%, #a47845 80%, #8d6030 100%);
  }
  .hero-figure {
    position: absolute; left: 96px; top: 322px; width: 232px; height: 370px;
    border-radius: 110px 110px 40px 40px;
    background: linear-gradient(180deg, #34509e 0%, var(--figure-blue) 30%, #c9a47c 32%, #c9a47c 42%, var(--figure-blue) 44%, var(--figure-blue-dark) 100%);
  }
  .title {
    font-family: "Bebas Neue", sans-serif; color: var(--title-ivory);
    text-transform: uppercase; line-height: 0.92; letter-spacing: 0.5px;
  }
  .back-cover .title { position: absolute; left: 38px; top: 84px; }
  .back-cover .title .line-1 { font-size: 72px; display: block; }
  .back-cover .title .line-2 { font-size: 49px; display: block; }
  .blurb {
    position: absolute; left: 38px; top: 225px; width: 402px;
    font-family: "Ubuntu", sans-serif; font-size: 14.4px; line-height: 18.5px;
    color: var(--body-text); text-align: justify;
  }
  .blurb p { margin-bottom: 18px; }
  .blurb .tagline { color: var(--tagline); text-align: left; margin-bottom: 14px; }
  .isbn-box { position: absolute; left: 280px; top: 594px; width: 166px; height: 99px; background: #fff; }
  .imprint {
    position: absolute; display: flex; align-items: center; gap: 4px;
    font-family: "Montserrat", sans-serif; font-weight: 600; color: var(--title-ivory);
  }
  .imprint .dot { width: 10px; height: 10px; border-radius: 50%; background: var(--mark-red); }
  .back-cover .imprint { left: 44px; top: 650px; font-size: 15px; }
  .front-cover .imprint { left: 388px; top: 650px; font-size: 15px; }
  .spine .imprint {
    left: 50%; top: 672px; transform: translateX(-50%) rotate(-90deg);
    font-size: 11px; white-space: nowrap;
  }
  .spine-author {
    position: absolute; left: 50%; top: 134px; transform: translate(-50%, -50%) rotate(-90deg);
    font-family: "Montserrat", sans-serif; font-weight: 500; font-size: 11px; line-height: 13px;
    color: var(--gold); white-space: nowrap; text-align: left;
  }
  .spine-title {
    position: absolute; left: 50%; top: 424px; transform: translate(-50%, -50%) rotate(-90deg);
    font-family: "Bebas Neue", sans-serif; font-size: 27px; color: var(--title-ivory); white-space: nowrap;
  }
  .front-text { position: absolute; left: 0; top: 0; width: 100%; text-align: center; }
  .author {
    margin-top: 42px; font-family: "Montserrat", sans-serif; font-weight: 600;
    font-size: 21px; color: var(--gold);
  }
  .front-cover .title { margin-top: 18px; }
  .front-cover .title .line-1 { font-size: 92px; display: block; }
  .front-cover .title .line-2 { font-size: 76px; display: block; }
  .subtitle {
    margin-top: 12px; font-family: "Montserrat", sans-serif; font-weight: 600;
    font-size: 30px; line-height: 32px; color: var(--gold);
  }
</style>
</head>
<body>
  <div class="cover">
    <section class="back-cover">
      <h2 class="title"><span class="line-1">Der Kreislauf</span><span class="line-2">der Nachfrage</span></h2>
      <div class="blurb">
        <p class="tagline">Die Ökonomie beginnt nicht beim Markt – sie beginnt bei Ihnen</p>
        <p>Dieses Buch behauptet etwas Unverschämtes: Unsere Wirtschaft basiert auf der stillen Erwartung, dass jemand anderer uns füttert.</p>
        <p>Wer das einmal sieht, versteht plötzlich Krisen, Macht und Wohlstand auf eine neue, fast unangenehme Weise.</p>
        <p>Konrad Edmund Wiesheimer dreht die Perspektive radikal um – vom Verbraucher aus gedacht, bis nichts mehr selbstverständlich bleibt.</p>
        <p>Ein Buch für alle, die nicht länger so tun wollen, als hätten sie mit dem Ganzen nichts zu tun</p>
      </div>
      <div class="isbn-box"></div>
      <div class="imprint"><span class="dot"></span>Q3T</div>
    </section>

    <section class="spine">
      <div class="spine-author">Konrad Edmund<br>Wiesheimer</div>
      <div class="spine-title">Der Kreislauf der Nachfrage</div>
      <div class="imprint">Q3T</div>
    </section>

    <section class="front-cover">
      <div class="front-photo" role="img" aria-label="Foto: Holzspielbrett mit bunten Spielfiguren und Würfel im unscharfen Hintergrund"></div>
      <div class="hero-figure" role="img" aria-label="Foto: blaue hölzerne Königsfigur mit Krone, Gabel und Messer auf dem Spielbrett"></div>
      <div class="front-text">
        <p class="author">Konrad Edmund Wiesheimer</p>
        <h1 class="title"><span class="line-1">Der Kreislauf</span><span class="line-2">der Nachfrage</span></h1>
        <p class="subtitle">Keiner bringt<br>uns das Brot</p>
      </div>
      <div class="imprint"><span class="dot"></span>Q3T</div>
    </section>
  </div>
</body>
</html>
```